Bright Path Therapies business cards and stationary

Need business cards and stationary designed to match previously made logo for for a new company based in Sydney NSW called 'Bright Path Therapies'.

We provide early intervention services and diagnostic assessment for children with disability and their families. I would like designs that are colourful and child friendly - possibly using feet/footprints/steps on a white background. The final design should communicate that we are family friendly, accepting and fun to work with.

Target Market(s)

Parents and Families
Teachers
Allied Health Professionals

Industry/Entity Type

Psychology

Contact Information for Business Card

Bright Path Therapies
www.brightpaththerapies-example.com
info@brightpaththerapies-example.com

Font styles to use
Sans Serif
Decorative
Script

Requirements
Must have
• Match the font and colour scheme of logo, along with footprint picture
Nice to have
• Clean and simple, while reflecting that I am working with families.
• Also- editable for when we make staff specific cards.

```html
<!DOCTYPE html>
<html lang="en">
<head>
<meta charset="utf-8">
<title>Bright Path Therapies – Business Card</title>
<link rel="stylesheet" href="https://fonts.googleapis.com/css2?family=Lato:wght@400;700&family=Amatic+SC:wght@700&display=swap">
<style>
  :root {
    --page: #2a2a2c;
    --card-white: #ffffff;
    --brand-blue: #2574bb;
    --brand-blue-deep: #1f66a8;
    --brand-red: #e8453a;
    --brand-green: #7cbb32;
    --brand-orange: #e88a1e;
    --text-grey: #555a60;
    --text-dark: #3a3d42;
  }
  * { box-sizing: border-box; margin: 0; padding: 0; }
  html, body { width: 1200px; height: 963px; overflow: hidden; }
  body {
    background: var(--page);
    font-family: "Lato", sans-serif;
    display: flex;
    flex-direction: column;
    align-items: center;
    justify-content: center;
    gap: 50px;
  }
  .card {
    position: relative;
    width: 640px;
    height: 366px;
    border-radius: 18px;
    overflow: hidden;
  }
  /* Front */
  .card-front { background: var(--card-white); }
  .card-front .waves { position: absolute; inset: 0; width: 100%; height: 100%; }
  .brand {
    position: absolute;
    left: 40px;
    top: 56px;
    display: flex;
    align-items: center;
    gap: 14px;
  }
  .brand-dot {
    width: 54px; height: 54px; border-radius: 50%;
    background: var(--brand-red);
  }
  .brand-name {
    font-family: "Lato", sans-serif;
    font-weight: 700;
    font-size: 26px;
    color: var(--brand-blue);
    letter-spacing: 0.5px;
  }
  .divider {
    position: absolute;
    left: 330px; top: 132px;
    width: 2px; height: 96px;
    background: var(--brand-green);
  }
  .contact {
    position: absolute;
    left: 350px; top: 128px;
  }
  .person-name {
    font-family: "Amatic SC", sans-serif;
    font-weight: 700;
    font-size: 30px;
    letter-spacing: 2px;
    color: var(--brand-green);
    line-height: 1;
  }
  .person-role {
    font-size: 13px; font-weight: 700;
    color: var(--text-dark);
    margin-bottom: 8px;
  }
  .contact-line {
    display: flex; align-items: center; gap: 8px;
    font-size: 12.5px; color: var(--text-grey);
    line-height: 20px;
  }
  .contact-line svg { width: 12px; height: 12px; flex: none; }
  .contact-line.web { color: var(--brand-blue); }
  /* Back */
  .card-back { background: var(--brand-blue); }
  .footprint-field {
    position: absolute; inset: 0;
    background: radial-gradient(circle at 30% 40%, var(--brand-blue) 0%, var(--brand-blue-deep) 100%);
  }
  .back-brand {
    position: absolute; inset: 0;
    display: flex; align-items: center; justify-content: center; gap: 18px;
  }
  .back-brand .brand-dot { width: 80px; height: 80px; background: #ffffff; }
  .back-brand .brand-name { color: #ffffff; font-size: 36px; }
</style>
</head>
<body>
  <section class="card card-front" aria-label="Business card front">
    <svg class="waves" viewBox="0 0 640 366" preserveAspectRatio="none" aria-hidden="true">
      <path d="M0 225 C120 250 200 330 250 366 L0 366 Z" fill="var(--brand-orange)"/>
      <path d="M0 212 C140 235 230 320 290 366 L0 366 Z" fill="var(--brand-blue)"/>
      <path d="M0 222 C130 250 210 330 270 366 L0 366 Z" fill="#ffffff"/>
      <path d="M0 238 C110 300 230 300 330 300 C420 300 500 330 540 366 L0 366 Z" fill="var(--brand-green)"/>
      <path d="M0 244 C110 306 230 308 330 310 C410 312 480 340 520 366 L0 366 Z" fill="#ffffff"/>
      <path d="M0 250 C110 312 230 318 330 320 C400 322 460 346 490 366 L0 366 Z" fill="var(--brand-red)"/>
    </svg>
    <div class="brand">
      <div class="brand-dot"></div>
      <div class="brand-name">Bright Path Therapies</div>
    </div>
    <div class="divider"></div>
    <div class="contact">
      <div class="person-name">Jordan M. Ellis</div>
      <div class="person-role">Founder</div>
      <div class="contact-line">
        <svg viewBox="0 0 12 12"><rect x="3" y="1" width="6" height="10" rx="1" fill="none" stroke="var(--brand-red)" stroke-width="1.4"/></svg>
        555-014-2087
      </div>
      <div class="contact-line">
        <svg viewBox="0 0 12 12"><rect x="1" y="2.5" width="10" height="7" fill="var(--brand-red)"/><path d="M1 2.5 L6 7 L11 2.5" fill="none" stroke="#fff" stroke-width="1"/></svg>
        info@brightpaththerapies-example.com
      </div>
      <div class="contact-line web">
        <svg viewBox="0 0 12 12"><circle cx="6" cy="6" r="5" fill="var(--brand-red)"/><path d="M1 6 H11 M6 1 V11" stroke="#fff" stroke-width="0.8"/></svg>
        www.brightpaththerapies-example.com
      </div>
    </div>
  </section>

  <section class="card card-back" aria-label="Business card back">
    <div class="footprint-field" role="img" aria-label="Faint scattered footprint pattern in darker blue"></div>
    <div class="back-brand">
      <div class="brand-dot"></div>
      <div class="brand-name">Bright Path Therapies</div>
    </div>
  </section>
</body>
</html>
```